Flyer for an pediatric sleep consultancy - to distribute to play and childcare centers etc.

I need a flyer that will attract the attention of parents with children between the age of babies to toddlers, who may be experiencing sleep issues. The flyer will be placed at places such as community centers, doctors room, play centers, kindergardens, etc.

My company is called "The Quiet Meadow Studio" and provides a sleep consultancy service. My service essentially provides a customized plan for parents to follow and general advice and guidance. It is not medical advice.

I like to the flyer to have an overall tone that is soft and peaceful with a clean and beautiful design, however can catch the attention of parents who may be struggling with their child's sleep issues and are sleep deprived. I would like photos with minimal text. The colour I use is a brownish rose. I will attach some of my designs to give you an idea. You can have a look at my homepage as well to get an idea about my esthetic direction and the colour. Although the colour of my page is a bit too brownish....

I will provide the text to appear in the flyer once I have a better idea of the layout that I prefer for the flyer. The text however wont be extensive, just some catchy points.

I want to direct people to my website which is www.quietmeadowstudio-example.com
I offer a first FREE evaluation call, to the parents, to get to know each other better, learn about their child's particular sleep problems and see if we are a good fit and can work together. I would like to have this information somehow on the flyer, so that the parents will contact me.
I also have a facebook page, which is: The Quiet Meadow Studio

I have a logo that I would like to appear on the flyer. I will attach the file once the uploader on art bazaar is fixed.

When I print the flyer - I like to print A5 SIZE ... please make sure the formatting is OK for this size.

Here are some text ideas. of course all of it would be too much, I guess. On the front of the flyer I would like to have some catchy phrase or something similar to get people interested and to want to know more. On the back there could be a bit more text and information. But I'm open too suggestions....
I'm not too sure about the wording yet. But here are some text that I might be use:

Is sleep an issue in your home?

Is your baby having trouble sleeping? ... are you?!
I can help!

Sleep, baby, sleep….

Teaching children how to sleep

The Quiet Meadow Studio is a pediatric sleep consultancy that specializes in helping parents with children who struggle to develop good and healthy sleep habits.
Disruptive sleep patterns or not enough sleep can affect the physical, mental and emotional development of your child.

Of course nobody plans to have a sleep problem, but habits can become easily ingrained and spiral quickly out of control and you can find yourself sleep deprived, desperate and not too sure what to do. You see all the other sleeping babies and wish there was someone who understood what you were going through?! Well, there is!

Contact me for a free 15 minute consultation.

This 15 minute „mini“ consultation is a chance to discuss your unique sleep challenges and sleep goals with me. I will provide you with an overview of how I will work with your family to achieve your wildest sleep dreams (goals).
Furthermore do I understand and believe that every child and their family is unique and there is no one size fits all!
I would love to have a chat with you and talk about how I can help make things easier for you and your family!

Do I need a sleep consultant for my child?
The answer is yes if:
- if your child will only fall asleep when nursing or bottle feeding
- if your child needs a dummy or other external aid, like being rocked, patted or taken for a care ride to fall asleep
- if your good night routine is a challenging and exhausting procedure instead of a relaxed and enjoyable moment for the whole family
- if sleep is a constant battle in your home which leaves you feeling frustrated and exhausted
- if your own lack of sleep is taking a toll on you and the whole family

What can I do for you?

I will:

- Guide you to set an age appropriate foundation for good sleep
- Create an individual sleep plan tailored especially to your child’s sleep needs and circumstances
- Help you to teach your childto go to sleep and get back to sleep independently during the night
- show you how to teach your child to take healthful, restorative naps
-Learn

Contact:

Marta Lindqvist
info@quietmeadowstudio-example.com
www.quietmeadowstudio-example.com
+34 612 380 574

Consultations in English, German or Spanish via Phone/Skype or home consultation

Reason: I have to go on a business trip and won't be able to choose a design until the deadline. During the trip I won't have time to give feedback and ask for changes. thank you

Target Market(s)

parents, sleep deprived mothers, young families, child care provider,

Industry/Entity Type

Baby Care

Contact Information for Business Card

Marta Lindqvist
pediatric sleep consultant
+34 612 380 574

```html
<!DOCTYPE html>
<html lang="en">
<head>
<meta charset="utf-8">
<title>The Quiet Meadow Studio – Flyer</title>
<link rel="stylesheet" href="https://fonts.googleapis.com/css2?family=Fjalla+One&family=Ropa+Sans&display=swap">
<style>
  :root {
    --backdrop: #2e0204;
    --paper: #ffffff;
    --heading-brown: #8a4a1f;
    --body-grey: #707070;
    --bullet-tan: #c39b6f;
    --contact-tan: rgba(206, 170, 134, 0.94);
    --icon-tan: #c79f78;
    --ring-rose: #e3c2b6;
    --white: #ffffff;
  }
  * { box-sizing: border-box; margin: 0; padding: 0; }
  html, body { width: 1000px; height: 1200px; overflow: hidden; background: var(--backdrop); }
  .canvas { position: relative; width: 1000px; height: 1200px; }
  .flyer {
    position: absolute; left: 103px; top: 36px; width: 807px; height: 1111px;
    overflow: hidden; background: var(--paper);
    font-family: "Ropa Sans", "Arial Narrow", sans-serif;
  }
  .photo-sleeping-baby {
    position: absolute; inset: 0;
    background:
      radial-gradient(ellipse at 40% 45%, #c9c9c9 0%, #b0b0b0 35%, #d8d8d8 65%, #f2f2f2 100%);
  }
  .rings { position: absolute; inset: 0; }
  .services-circle {
    position: absolute; left: 272px; top: 9px; width: 570px; height: 570px;
    border-radius: 50%; background: rgba(255, 255, 255, 0.82);
  }
  .contact-circle {
    position: absolute; left: -18px; top: 704px; width: 490px; height: 490px;
    border-radius: 50%; background: var(--contact-tan);
  }
  .services-title {
    position: absolute; left: 455px; top: 34px;
    font-family: "Fjalla One", Impact, sans-serif; font-size: 27px;
    color: var(--heading-brown); letter-spacing: 0.5px;
  }
  .services-list { position: absolute; left: 382px; top: 74px; width: 400px; list-style: none; }
  .services-list li {
    position: relative; padding-left: 23px; font-size: 22px; line-height: 27px;
    color: var(--body-grey); margin-bottom: 26px;
  }
  .services-list li::before {
    content: ""; position: absolute; left: 1px; top: 9px; width: 12px; height: 12px;
    border-radius: 50%; background: var(--bullet-tan);
  }
  .brand-name {
    position: absolute; left: 503px; top: 502px; font-size: 20px; color: #6a4a3e;
  }
  .contact-title {
    position: absolute; left: 0; width: 420px; top: 756px; text-align: center;
    font-family: "Fjalla One", Impact, sans-serif; font-size: 34px; color: var(--white);
  }
  .contact-name { position: absolute; left: 82px; top: 818px; font-size: 27px; color: var(--white); }
  .contact-line {
    position: absolute; left: 52px; display: flex; align-items: center; gap: 8px;
    font-size: 21px; color: var(--white);
  }
  .contact-line svg { width: 24px; height: 24px; flex: none; }
  .languages-label { position: absolute; left: 52px; top: 954px; font-size: 20px; color: var(--white); }
  .language {
    position: absolute; left: 52px; font-size: 20px; letter-spacing: 1.5px; color: var(--white);
    display: flex; align-items: center;
  }
  .language svg { position: absolute; left: 107px; width: 36px; height: 22px; }
  .modes { position: absolute; left: 222px; top: 1015px; display: flex; gap: 12px; }
  .modes svg { width: 44px; height: 44px; }
</style>
</head>
<body>
<div class="canvas">
  <div class="flyer">
    <div class="photo-sleeping-baby" role="img" aria-label="Black and white photo of a newborn baby sleeping peacefully with a tiny hand near its face"></div>

    <div class="services-circle"></div>
    <div class="contact-circle"></div>

    <svg class="rings" viewBox="0 0 807 1111" aria-hidden="true">
      <circle cx="565" cy="288" r="292" fill="none" stroke="var(--ring-rose)" stroke-width="2"/>
      <circle cx="232" cy="946" r="250" fill="none" stroke="var(--ring-rose)" stroke-width="2"/>
    </svg>

    <h2 class="services-title">WHAT CAN I DO FOR YOU?</h2>
    <ul class="services-list">
      <li>Guide you to set an age appropriate foundation for good sleep</li>
      <li>Create an individual sleep plan tailored especially to your child’s sleep needs and circumstances</li>
      <li>Help you to teach your child to go to sleep and get back to sleep independently during the night</li>
      <li>Show you how to teach your child to take healthful, restorative naps</li>
      <li>Learn</li>
    </ul>
    <div class="brand-name">The Quiet Meadow Studio</div>

    <h2 class="contact-title">CONTACT</h2>
    <div class="contact-name">Marta Lindqvist</div>

    <div class="contact-line" style="top:852px">
      <svg viewBox="0 0 24 24" aria-hidden="true"><rect x="1" y="5" width="22" height="15" rx="2" fill="var(--icon-tan)"/><path d="M2 6 L12 14 L22 6" fill="none" stroke="#e9d3bd" stroke-width="1.6"/></svg>
      info@quietmeadowstudio-example.com
    </div>
    <div class="contact-line" style="top:887px">
      <svg viewBox="0 0 24 24" aria-hidden="true"><circle cx="12" cy="12" r="11" fill="var(--icon-tan)"/><path d="M6 8c3 0 4 2 3 4s2 3 2 6M14 4c0 3 3 3 5 5" fill="none" stroke="#e9d3bd" stroke-width="1.6"/></svg>
      www.quietmeadowstudio-example.com
    </div>
    <div class="contact-line" style="top:921px">
      <svg viewBox="0 0 24 24" aria-hidden="true"><rect x="1" y="1" width="22" height="22" rx="5" fill="var(--icon-tan)"/><path d="M8 5l2 4-2 1.5c1 2.5 3 4.5 5.5 5.5L15 14l4 2-1 3c-6 0-12-6-12-12z" fill="#e9d3bd"/></svg>
      +34 612 380 574
    </div>

    <div class="languages-label">Consultations in</div>
    <div class="language" style="top:981px">ENGLISH
      <svg viewBox="0 0 60 36" aria-hidden="true"><rect width="60" height="36" fill="#1f3a8a"/><path d="M0 0L60 36M60 0L0 36" stroke="#fff" stroke-width="8"/><path d="M0 0L60 36M60 0L0 36" stroke="#c8102e" stroke-width="3"/><path d="M30 0V36M0 18H60" stroke="#fff" stroke-width="11"/><path d="M30 0V36M0 18H60" stroke="#c8102e" stroke-width="6"/></svg>
    </div>
    <div class="language" style="top:1008px">GERMAN
      <svg viewBox="0 0 60 36" aria-hidden="true"><rect width="60" height="12" fill="#000"/><rect y="12" width="60" height="12" fill="#dd0000"/><rect y="24" width="60" height="12" fill="#ffce00"/></svg>
    </div>
    <div class="language" style="top:1035px">SPANISH
      <svg viewBox="0 0 60 36" aria-hidden="true"><rect width="60" height="36" fill="#c60b1e"/><rect y="9" width="60" height="18" fill="#ffc400"/></svg>
    </div>

    <div class="modes">
      <svg viewBox="0 0 44 44" role="img" aria-label="Video call"><circle cx="22" cy="22" r="20" fill="var(--icon-tan)"/></svg>
      <svg viewBox="0 0 44 44" role="img" aria-label="Phone"><rect x="2" y="2" width="40" height="40" rx="9" fill="var(--icon-tan)"/><path d="M14 10l4 7-3 2.5c2 4 5 7 9 9L26.5 26l7 4-2 5c-11 0-21-10-21-21z" fill="#e9d3bd"/></svg>
      <svg viewBox="0 0 44 44" role="img" aria-label="Home consultation"><path d="M22 5L2 23h6v16h10V29h8v10h10V23h6z" fill="var(--icon-tan)"/></svg>
    </div>
  </div>
</div>
</body>
</html>
```